Business Card Design

A logo and business card design is required for a new podiatry business based on the Great Ocean Road, Victoria, Australia. The business will provide broad array of podiatry services to communities along the coast.

A distinctive design is sought that represents both professional allied health service delivery and the iconic location of the service, where the ocean meets the Otway ranges. Colours representative of the ocean blues, greens of the local forrest would be desirable.

Target Market(s)

GP's, other allied health professionals, members of the community with foot complaints

Industry/Entity Type

Health

Contact Information for Business Card

Tidewater Bend Podiatry
Gareth Linwell
B.Pod B App Sci (HM)
Phone: 0400 718 306
Email: tidewaterbendpodiatry@mailbrook.net

Requirements
Must have
• On the back of the card room allocated for appointment times.
Nice to have
• Would like the logo to incorporate a foot and the elements of the coast, whether it be ocean &/or the unique elements of the coast and the great ocean road.

```html
<!DOCTYPE html>
<html lang="en">
<head>
<meta charset="utf-8">
<title>Tidewater Bend Podiatry – Business Card</title>
<link rel="stylesheet" href="https://fonts.googleapis.com/css2?family=Open+Sans:wght@400;600&display=swap">
<style>
  :root {
    --backdrop: #e4e5e7;
    --card-light: #4a4b4e;
    --card-dark: #2a2b2d;
    --accent: #1aa6ea;
    --text: #d9dadc;
    --text-soft: #c4c5c8;
    --icon: #ffffff;
  }
  * { margin: 0; padding: 0; box-sizing: border-box; }
  html, body {
    width: 1200px; height: 816px; overflow: hidden;
    background: var(--backdrop);
    font-family: "Open Sans", Arial, sans-serif;
  }
  .card {
    position: absolute; left: 75px; top: 108px;
    width: 1050px; height: 600px; border-radius: 40px;
    background: radial-gradient(ellipse at 55% 45%, var(--card-light) 0%, #393a3d 45%, var(--card-dark) 100%);
    overflow: hidden;
    box-shadow: 0 10px 30px rgba(0,0,0,.25);
  }
  .side-band {
    position: absolute; left: 62px; top: 0;
    width: 62px; height: 510px;
    background: var(--accent);
    border-radius: 0 0 31px 31px;
  }
  .band-icon {
    position: absolute; left: 77px; width: 32px; height: 32px;
    fill: var(--icon);
  }
  .icon-person { top: 92px; }
  .icon-phone  { top: 318px; }
  .icon-mail   { top: 372px; }
  .icon-globe  { top: 412px; }
  .icon-home   { top: 466px; }
  .holder { position: absolute; left: 150px; top: 78px; color: var(--text); }
  .holder-name { font-size: 31px; font-weight: 400; line-height: 1.15; }
  .holder-title { font-size: 27px; font-weight: 400; letter-spacing: .5px; text-transform: uppercase; }
  .contact { position: absolute; left: 150px; color: var(--text-soft); font-size: 22px; line-height: 1.45; }
  .contact-phone { top: 314px; }
  .contact-online { top: 366px; }
  .contact-address { top: 456px; }
  .brand {
    position: absolute; left: 440px; top: 186px;
    display: flex; align-items: center; gap: 16px;
  }
  .brand-dot { width: 30px; height: 30px; border-radius: 50%; background: var(--accent); }
  .brand-name {
    color: var(--accent); font-size: 36px; font-weight: 600; letter-spacing: 1px;
  }
  .edge-tab {
    position: absolute; right: 0; top: 228px;
    width: 52px; height: 26px; background: var(--accent);
  }
</style>
</head>
<body>
  <div class="card">
    <div class="side-band"></div>

    <svg class="band-icon icon-person" viewBox="0 0 24 24" aria-hidden="true"><circle cx="12" cy="8" r="4.5"/><path d="M3 21c0-5 4-8 9-8s9 3 9 8z"/></svg>
    <svg class="band-icon icon-phone" viewBox="0 0 24 24" aria-hidden="true"><path d="M6.6 3.5l2.6 3.4-1.7 2.2a12 12 0 0 0 7.4 7.4l2.2-1.7 3.4 2.6-1.6 3.1C11 20.2 3.8 13 3.5 5.1z"/></svg>
    <svg class="band-icon icon-mail" viewBox="0 0 24 24" aria-hidden="true"><path d="M3 6h18v12H3z M3 6l9 7 9-7" fill="none" stroke="#fff" stroke-width="2"/></svg>
    <svg class="band-icon icon-globe" viewBox="0 0 24 24" aria-hidden="true"><g fill="none" stroke="#fff" stroke-width="1.8"><circle cx="12" cy="12" r="9"/><ellipse cx="12" cy="12" rx="4" ry="9"/><path d="M3 12h18M5 7h14M5 17h14"/></g></svg>
    <svg class="band-icon icon-home" viewBox="0 0 24 24" aria-hidden="true"><path d="M12 3l10 9h-3v9h-5v-6h-4v6H5v-9H2z"/></svg>

    <div class="holder">
      <p class="holder-name">Gareth Linwell</p>
      <p class="holder-title">General Manager</p>
    </div>

    <p class="contact contact-phone">0400 718 306</p>
    <div class="contact contact-online">
      <p>tidewaterbendpodiatry@mailbrook.net</p>
      <p>www.tidewaterbend.net</p>
    </div>
    <div class="contact contact-address">
      <p>18 Harbour Crest Rd,</p>
      <p>Lorne Bay VIC, Australia</p>
    </div>

    <div class="brand">
      <span class="brand-dot"></span>
      <span class="brand-name">Tidewater Bend Podiatry</span>
    </div>

    <div class="edge-tab"></div>
  </div>
</body>
</html>
```